Design some Business Cards for my business running bachelorette parties

Hi, I am starting a business on the central coast running bachelorette parties and need some kick ass business cards - you know ones that make people sit up and go Wow!! I am also putting together a website for my business as well - so if your design is really kick ass we can discuss how much you would charge to let me use it on my website - or possibly to do my website. :)

I am looking for classy, fun, off beat, unique - something with some personality - like me :) Please feel free to email me questions and bounce ideas off me. And have fun!!!!

```html
<!DOCTYPE html>
<html lang="en">
<head>
<meta charset="utf-8">
<title>Bachelorette Parties – Business Cards</title>
<link rel="stylesheet" href="https://fonts.googleapis.com/css2?family=Libre+Baskerville:ital,wght@0,700;1,400&family=Sue+Ellen+Francisco&display=swap">
<style>
  :root {
    --backdrop: #5a3220;
    --card-white: #ffffff;
    --panel-pink: #f1c6d3;
    --hot-pink: #e8237f;
    --ink-black: #111111;
    --text-grey: #555555;
    --band-dark: #2c2c2c;
    --band-light: #9a9a9a;
  }
  * { margin: 0; padding: 0; box-sizing: border-box; }
  html, body { width: 1200px; height: 749px; overflow: hidden; }
  body { background: var(--backdrop); position: relative; }

  .card {
    position: absolute;
    width: 476px;
    height: 272px;
    background: var(--card-white);
    overflow: hidden;
  }
  .card--front { left: 141px; top: 99px; }
  .card--back  { left: 633px; top: 407px; }

  .stripe-band {
    position: absolute;
    left: 0; width: 100%;
    background: linear-gradient(90deg, var(--band-dark), var(--band-light) 50%, var(--band-dark));
  }
  .stripe-band--top { top: 0; height: 38px; }
  .stripe-band--bottom { bottom: 0; height: 35px; }

  .pink-rule {
    position: absolute; left: 0; width: 100%; height: 5px;
    background: var(--hot-pink);
  }
  .pink-rule--top { top: 38px; }
  .pink-rule--bottom { bottom: 38px; }

  .panel {
    position: absolute; left: 0; width: 100%;
    background: var(--panel-pink);
  }
  .card--front .panel { top: 46px; height: 182px; }
  .card--back .panel { top: 46px; height: 185px; }

  .emblem {
    position: absolute;
    width: 74px; height: 74px;
    border-radius: 50%;
    background: var(--ink-black);
    border: 4px solid var(--hot-pink);
    box-shadow: 0 0 0 2px var(--card-white);
    left: 184px;
  }
  .card--front .emblem { top: 9px; }
  .card--back .emblem { top: 6px; }

  .brand-title {
    position: absolute; left: 73px; top: 114px;
    font-family: "Libre Baskerville", Georgia, serif;
    font-weight: 700;
    font-size: 33px;
    letter-spacing: -0.5px;
    color: var(--hot-pink);
    line-height: 1;
  }
  .brand-sub {
    position: absolute; left: 285px; top: 147px;
    font-family: "Sue Ellen Francisco", cursive;
    font-weight: 400;
    font-size: 56px;
    letter-spacing: 4px;
    color: var(--text-grey);
    line-height: 1;
    transform: rotate(-5deg);
    transform-origin: left bottom;
  }

  .contact-heading {
    position: absolute; left: 138px; top: 84px;
    font-family: "Sue Ellen Francisco", cursive;
    font-weight: 400;
    font-size: 46px;
    color: var(--text-grey);
    line-height: 1;
    letter-spacing: 3px;
  }
  .contact-item {
    position: absolute;
    display: flex; align-items: center; gap: 12px;
    font-family: "Libre Baskerville", Georgia, serif;
    font-style: italic;
    font-size: 14px;
    color: var(--text-grey);
  }
  .contact-icon {
    width: 27px; height: 27px;
    border-radius: 4px;
    background: var(--hot-pink);
    display: flex; align-items: center; justify-content: center;
  }
  .contact-icon svg { width: 17px; height: 17px; }
  .contact-item--email { left: 15px; top: 142px; }
  .contact-item--phone { left: 15px; top: 181px; }
  .contact-item--address { left: 241px; top: 142px; }
  .contact-item--web { left: 241px; top: 181px; }
</style>
</head>
<body>

<section class="card card--front">
  <div class="stripe-band stripe-band--top" role="img" aria-label="Black and white zebra print band"></div>
  <div class="pink-rule pink-rule--top"></div>
  <div class="panel"></div>
  <div class="pink-rule pink-rule--bottom"></div>
  <div class="stripe-band stripe-band--bottom" role="img" aria-label="Black and white zebra print band"></div>
  <div class="emblem"></div>
  <h1 class="brand-title">BACHELORETTE</h1>
  <p class="brand-sub">parties</p>
</section>

<section class="card card--back">
  <div class="stripe-band stripe-band--top" role="img" aria-label="Black and white zebra print band"></div>
  <div class="pink-rule pink-rule--top"></div>
  <div class="panel"></div>
  <div class="pink-rule pink-rule--bottom"></div>
  <div class="stripe-band stripe-band--bottom" role="img" aria-label="Black and white zebra print band"></div>
  <div class="emblem"></div>
  <h2 class="contact-heading">Contact us:</h2>

  <div class="contact-item contact-item--email">
    <span class="contact-icon">
      <svg viewBox="0 0 24 24" fill="none" stroke="#fff" stroke-width="2.4" stroke-linecap="round">
        <circle cx="12" cy="12" r="4"/>
        <path d="M16 8v5.5a2.5 2.5 0 0 0 5 0V12a9 9 0 1 0-3.5 7.1"/>
      </svg>
    </span>
    <span>hello@shorelinehens.com</span>
  </div>

  <div class="contact-item contact-item--phone">
    <span class="contact-icon">
      <svg viewBox="0 0 24 24" fill="#fff">
        <path d="M6.6 10.8a15.1 15.1 0 0 0 6.6 6.6l2.2-2.2a1 1 0 0 1 1-.25 11.4 11.4 0 0 0 3.6.57 1 1 0 0 1 1 1V20a1 1 0 0 1-1 1A17 17 0 0 1 3 4a1 1 0 0 1 1-1h3.5a1 1 0 0 1 1 1c0 1.250.2 2.45.57 3.57a1 1 0 0 1-.25 1z"/>
      </svg>
    </span>
    <span>555 014 8823</span>
  </div>

  <div class="contact-item contact-item--address">
    <span class="contact-icon">
      <svg viewBox="0 0 24 24" fill="#fff">
        <path d="M12 3 2 12h3v9h5v-6h4v6h5v-9h3z"/>
      </svg>
    </span>
    <span>42 Seabreeze Drive, NY</span>
  </div>

  <div class="contact-item contact-item--web">
    <span class="contact-icon">
      <svg viewBox="0 0 24 24" fill="none" stroke="#fff" stroke-width="1.8">
        <circle cx="12" cy="12" r="9"/>
        <ellipse cx="12" cy="12" rx="4" ry="9"/>
        <path d="M3 12h18M4.5 7.5h15M4.5 16.5h15"/>
      </svg>
    </span>
    <span>www.shorelinehens.com</span>
  </div>
</section>

</body>
</html>
```